Stonebay Towing Business Card

Towing
Accident towing
Mechanical breakdown
Insurance, salvage and recovery
4wd off road towing
Light & Heavy towing
8347 2516
24 hour business 7 days

Logo can be whole size on front

Industry/Entity Type

Towing/ transport

Contact Information for Business Card

The above

```html
<!DOCTYPE html>
<html lang="en">
<head>
<meta charset="utf-8">
<title>Stonebay Towing Business Card</title>
<link href="https://fonts.googleapis.com/css2?family=Roboto:wght@400;500;700&display=swap" rel="stylesheet">
<style>
  :root {
    --backdrop: #787878;
    --card: #ffffff;
    --brand-red: #d6232b;
    --ink: #111111;
    --rule: #111111;
    --on-red: #ffffff;
  }
  * { margin: 0; padding: 0; box-sizing: border-box; }
  html, body {
    width: 1200px;
    height: 1200px;
    overflow: hidden;
    background: var(--backdrop);
    font-family: "Roboto", Arial, sans-serif;
  }
  .canvas {
    position: relative;
    width: 1200px;
    height: 1200px;
  }
  .card {
    position: absolute;
    left: 165px;
    width: 869px;
    height: 508px;
    background: var(--card);
    box-shadow: 6px 8px 14px rgba(0, 0, 0, 0.35);
    overflow: hidden;
  }
  .card--info { top: 76px; }
  .card--brand { top: 626px; }

  .wordmark {
    position: absolute;
    color: var(--brand-red);
    font-weight: 700;
    white-space: nowrap;
    text-align: center;
    line-height: 1;
  }
  .card--info .wordmark {
    left: 76px;
    top: 78px;
    width: 300px;
    font-size: 38px;
  }
  .card--brand .wordmark {
    left: 0;
    right: 0;
    top: 218px;
    font-size: 68px;
  }

  .phone-band {
    position: absolute;
    left: 503px;
    top: 98px;
    width: 366px;
    height: 86px;
    background: var(--brand-red);
    display: flex;
    align-items: center;
    padding-left: 25px;
    gap: 18px;
    color: var(--on-red);
    font-size: 42px;
    font-weight: 500;
    letter-spacing: 0.5px;
  }
  .phone-band svg { width: 32px; height: 32px; fill: var(--on-red); }

  .divider {
    position: absolute;
    left: 105px;
    top: 295px;
    width: 658px;
    height: 3px;
    background: var(--rule);
  }

  .services {
    position: absolute;
    left: 0;
    right: 0;
    top: 342px;
    text-align: center;
    list-style: none;
    color: var(--ink);
    font-size: 23px;
    line-height: 34px;
    font-weight: 400;
  }
</style>
</head>
<body>
  <main class="canvas">
    <section class="card card--info">
      <div class="wordmark">Stonebay Towing</div>
      <div class="phone-band">
        <span class="phone-number">8347 2516</span>
        <svg viewBox="0 0 24 24" aria-hidden="true"><path d="M6.6 10.8c1.4 2.8 3.8 5.1 6.6 6.6l2.2-2.2c.3-.3.7-.4 1-.2 1.1.4 2.3.6 3.6.6.6 0 1 .4 1 1V20c0 .6-.4 1-1 1C10.6 21 3 13.4 3 4c0-.6.4-1 1-1h3.5c.6 0 1 .4 1 1 0 1.3.2 2.5.6 3.6.1.3 0 .7-.2 1L6.6 10.8z"/></svg>
      </div>
      <div class="divider"></div>
      <ul class="services">
        <li>Towing | Accident towing | Mechanical breakdown</li>
        <li>Insurance, salvage and recovery | 4wd off road towing</li>
        <li>Light &amp; Heavy towing</li>
      </ul>
    </section>
    <section class="card card--brand">
      <div class="wordmark">Stonebay Towing</div>
    </section>
  </main>
</body>
</html>
```